Meridane Works, Inc. - Update our Website

Meridane Works needs a website to help our customers to navigate through our services efficiently. Our existing website is at www.meridwork.example

We would like to explain our services with content and pictures (photographs) that distinguishes our products and services from our competition.

The website design must implement a strategy to focus on our Contract Labeling services.

With this new design we would like to attract new customers and ensure that our existing customers are fully informed with our latest offerings.

```html
<!DOCTYPE html>
<html lang="en">
<head>
<meta charset="utf-8">
<title>Meridane Works, Inc.</title>
<link rel="stylesheet" href="https://fonts.googleapis.com/css2?family=Open+Sans:wght@400;600;700&family=Lato:wght@400;700&display=swap">
<style>
:root{
  --ink:#333;
  --muted:#555;
  --green:#8dc63f;
  --green-dark:#5a9a1a;
  --orange:#e4731d;
  --navy:#124f7c;
  --red:#b0121b;
  --footer:#2c2c2c;
  --footer-deep:#1e1e1e;
  --footer-text:#cfcfcf;
  --line:#dcdcdc;
}
*{margin:0;padding:0;box-sizing:border-box}
html,body{width:971px;height:1200px;overflow:hidden;background:#fff}
body{position:relative;font-family:"Lato",sans-serif;color:var(--ink)}
.abs{position:absolute}
.topline{left:0;top:0;width:971px;height:3px;background:#2a3640}

.brand{left:114px;top:28px;display:flex;align-items:center;gap:12px}
.brand-dot{width:52px;height:52px;border-radius:50%;background:var(--green)}
.brand-name{font-family:"Open Sans",sans-serif;font-weight:700;font-size:21px;color:#1b1b1b;letter-spacing:.5px}

.callus{right:114px;top:32px;font-family:"Open Sans",sans-serif;font-size:14px;color:#333;display:flex;align-items:center;gap:5px}
.callus b{font-weight:600;font-size:13px}
.search{left:688px;top:69px;width:169px;height:19px;border:1px solid #c9c9c9;border-radius:4px;background:linear-gradient(#f4f4f4,#e8e8e8);font-size:8px;font-style:italic;color:#999;padding:4px 10px}
.search svg{position:absolute;right:7px;top:3px}

.nav{left:114px;top:108px;width:743px;height:33px;background:#fff;box-shadow:0 0 4px rgba(0,0,0,.25);padding:3px}
.nav ul{list-style:none;display:flex;justify-content:space-between;align-items:center;height:27px;background:var(--green);padding:0 10px;font-family:"Open Sans",sans-serif;font-size:10.5px;font-weight:600;color:#fff}

.hero{left:114px;top:146px;width:744px;height:316px;border:1px solid #d4d4d4;background:#fff;padding:4px;box-shadow:0 14px 12px -12px rgba(0,0,0,.35)}
.hero-img{width:100%;height:100%;background:linear-gradient(160deg,#2e4a5c 0%,#7fb6c4 30%,#d8eef2 60%,#f2f7f8 100%)}
.dots{left:420px;top:436px;width:132px;height:22px;background:#b6dc86;clip-path:polygon(12% 0,88% 0,100% 100%,0 100%);display:flex;justify-content:center;align-items:center;gap:9px}
.dots i{width:11px;height:11px;border-radius:50%;background:#555}
.dots i:first-child{background:#222}

.feature{top:502px;width:236px;height:175px;border:1px solid var(--line);text-align:center}
.feature h2{font-family:"Open Sans",sans-serif;font-weight:400;font-size:12.5px;height:37px;line-height:51px;margin:0 6px;border-bottom:1px solid var(--line)}
.feature .icon{width:60px;height:60px;border-radius:50%;margin:10px auto 0;display:flex;align-items:center;justify-content:center}
.feature p{font-size:9.5px;line-height:13.5px;color:#444;margin-top:18px;padding:0 4px}

.section-title{left:114px;top:706px;font-family:"Open Sans",sans-serif;font-weight:400;font-size:13px;color:#444}
.arrow{top:706px;width:15px;height:15px;border-radius:50%;border:1px solid #bbb;background:linear-gradient(#fff,#e5e5e5)}

.product{top:743px;width:226px;text-align:center}
.product .frame{height:130px;border:1px solid #d6d6d6;padding:3px;background:#fff}
.product .photo{width:100%;height:100%}
.product h3{font-family:"Open Sans",sans-serif;font-weight:600;font-size:10px;color:#1f8a3a;margin-top:10px}
.product p{font-size:9.5px;line-height:15px;color:#333;margin-top:5px}
.product a{display:block;font-size:10px;color:var(--red);text-decoration:none;margin-top:3px}

.footer{left:0;top:970px;width:971px;height:183px;background:var(--footer)}
.footer-bottom{left:0;top:1153px;width:971px;height:47px;background:var(--footer-deep)}
.fcol{top:988px;color:var(--footer-text)}
.fcol h4{font-weight:400;font-size:14px;color:#9a9a9a;margin-bottom:10px}
.fcol li{list-style:none;font-size:10px;line-height:21.2px}
.divider{top:992px;width:1px;height:146px;background:#555}
.tweet{font-size:9.5px;line-height:16.5px;width:230px}
.tweet small{display:block;font-size:9px;margin:4px 0 11px}
.social li{display:flex;align-items:center;gap:9px;line-height:28px}
.social i{width:24px;height:24px;border-radius:50%;background:#f2f2f2}
.copy{left:117px;top:1171px;font-size:9px;color:#8a8a8a}
</style>
</head>
<body>
<div class="abs topline"></div>

<div class="abs brand"><span class="brand-dot"></span><span class="brand-name">MERIDANE WORKS, INC.</span></div>

<div class="abs callus">
  <svg width="15" height="11" viewBox="0 0 15 11"><path d="M1 4c0-3 13-3 13 0v1h-3V4H4v1H1z M3 6h9l1 5H2z" fill="#444"/></svg>
  <b>Call Us:</b> (555) 010-0199
</div>
<div class="abs search">Search...
  <svg width="13" height="13" viewBox="0 0 13 13"><circle cx="5" cy="5" r="3.8" fill="none" stroke="#333" stroke-width="1.6"/><path d="M8 8l4 4" stroke="#333" stroke-width="2"/></svg>
</div>

<nav class="abs nav"><ul>
  <li>HOME</li><li>WHY COACHING</li><li>ABOUT</li><li>SERVICES</li><li>CLIENTS</li><li>RESOURCES</li><li>CONTACT</li><li>MORE</li>
</ul></nav>

<div class="abs hero"><div class="hero-img" role="img" aria-label="Photo of a hand using a computer mouse with overlaid data charts"></div></div>
<div class="abs dots"><i></i><i></i><i></i><i></i></div>

<section class="abs feature" style="left:114px">
  <h2 style="color:var(--orange)">MERISERV</h2>
  <div class="icon" style="background:var(--orange)">
    <svg width="34" height="30" viewBox="0 0 34 30"><rect x="8" y="1" width="18" height="8" fill="#fff"/><rect x="1" y="10" width="32" height="13" rx="3" fill="#fff"/><rect x="8" y="18" width="18" height="11" fill="#fff" stroke="var(--orange)" stroke-width="2"/><path d="M11 22h12M11 25h12" stroke="var(--orange)" stroke-width="1.5"/></svg>
  </div>
  <p>Lerspiciatis unde omnis iste natus error sit voluptatem accusantium doloremque laudantium, totam rem aperiam, eaque ipsa quae ab illo inventore</p>
</section>
<section class="abs feature" style="left:368px">
  <h2 style="color:var(--navy)">MERIBOOK</h2>
  <div class="icon" style="background:var(--navy)">
    <svg width="30" height="36" viewBox="0 0 30 36"><rect x="2" y="1" width="17" height="32" rx="3" fill="#fff"/><rect x="5" y="6" width="11" height="20" fill="var(--navy)"/><circle cx="20" cy="17" r="7" fill="#fff" stroke="var(--navy)" stroke-width="2"/><circle cx="20" cy="17" r="2.5" fill="var(--navy)"/></svg>
  </div>
  <p>Lerspiciatis unde omnis iste natus error sit voluptatem accusantium doloremque laudantium, totam rem aperiam, eaque ipsa quae ab illo inventore</p>
</section>
<section class="abs feature" style="left:622px">
  <h2 style="color:var(--green-dark)">CLINICAL RANDOMIZATIONS</h2>
  <div class="icon" style="background:var(--green-dark)">
    <svg width="32" height="32" viewBox="0 0 32 32"><g fill="#fff"><circle cx="16" cy="16" r="10"/><rect x="13" y="1" width="6" height="30" rx="1"/><rect x="1" y="13" width="30" height="6" rx="1"/><rect x="13" y="1" width="6" height="30" rx="1" transform="rotate(45 16 16)"/><rect x="13" y="1" width="6" height="30" rx="1" transform="rotate(-45 16 16)"/></g><circle cx="16" cy="16" r="4" fill="var(--green-dark)"/></svg>
  </div>
  <p>Lerspiciatis unde omnis iste natus error sit voluptatem accusantium doloremque laudantium, totam rem aperiam, eaque ipsa quae ab illo inventore</p>
</section>

<h2 class="abs section-title">SOFTWARE PRODUCTS / SERVICES</h2>
<div class="abs arrow" style="left:823px"><svg width="13" height="13" viewBox="0 0 13 13"><path d="M8 4v5L4.5 6.5z" fill="#111"/></svg></div>
<div class="abs arrow" style="left:842px"><svg width="13" height="13" viewBox="0 0 13 13"><path d="M5 4v5l3.5-2.5z" fill="#111"/></svg></div>

<article class="abs product" style="left:114px">
  <div class="frame"><div class="photo" role="img" aria-label="Photo of a scientist in a laboratory with shelves of bottles" style="background:linear-gradient(90deg,#d9dcdf,#f1f2f3 60%,#dfe2e5)"></div></div>
  <h3>MERIPRO</h3>
  <p>MeriPro Label is the industry's leading clinical label<br>generation system offering superior</p>
  <a href="#">(Click Here)</a>
</article>
<article class="abs product" style="left:372px">
  <div class="frame"><div class="photo" role="img" aria-label="Photo of a bright modern laboratory interior" style="background:linear-gradient(180deg,#cfd9f0,#a8b9e2 55%,#7f95c8)"></div></div>
  <h3>SOFTWARE VALIDATION SERVICES</h3>
  <p>Meridane Works offers software validation services<br>for the FDA regulated</p>
  <a href="#">(Click Here)</a>
</article>
<article class="abs product" style="left:631px">
  <div class="frame"><div class="photo" role="img" aria-label="Photo of a lab worker in protective gear holding a test tube" style="background:linear-gradient(90deg,#e6e8ea,#c8ccd0 45%,#9fb3a9 75%,#d3d6d8)"></div></div>
  <h3>MERISTOCK</h3>
  <p>MeriStock is a premium line of label products that<br>we supply to the pharmaceutical industry.</p>
  <a href="#">(Click Here)</a>
</article>

<footer>
  <div class="abs footer"></div>
  <div class="abs footer-bottom"></div>
  <div class="abs fcol" style="left:117px"><h4>COMPANY</h4><ul><li>Company Overview</li><li>About Us</li><li>Services Provide</li><li>Our Process</li><li>Our Clients</li></ul></div>
  <div class="abs divider" style="left:251px"></div>
  <div class="abs fcol" style="left:289px"><h4>WHAT WE DO</h4><ul><li>Value proposition</li><li>Our work</li><li>Testimonials</li><li>Faq</li><li>Contact us</li></ul></div>
  <div class="abs divider" style="left:420px"></div>
  <div class="abs fcol" style="left:458px;top:987px"><h4 style="margin-bottom:8px">CHIRPER FEED</h4>
    <div class="tweet">Nunc tempus felis vitae urna. Vivamus porttitor, g, purus nisi eleifend libero, a tempus<small>Posted 3 hours ago</small></div>
    <div class="tweet">Nunc tempus felis vitae urna. Vivamus porttitor, g, purus nisi eleifend libero, a tempus<small>Posted 3 hours ago</small></div>
  </div>
  <div class="abs divider" style="left:705px"></div>
  <div class="abs fcol" style="left:747px;top:987px"><h4 style="margin-bottom:6px">GET CONNECTED</h4>
    <ul class="social"><li><i></i>Friendbook</li><li><i></i>Chirper</li><li><i></i>WorkNet</li><li><i></i>RSS</li></ul>
  </div>
  <p class="abs copy">© 2014 Meridane Works, Inc. All rights reserved.</p>
</footer>
</body>
</html>
```